Business Cards for Live Events Company

We are Zoomb'r.
We are Looking for a business card design for our live entertainment technical company.
We design lighting, video, and audio for Theatre, Live events, and Concerts.

We also hire out technical equipment for these, which includes: Lights, Special FX, Audio, Video, Projection, LED Screens, Rigging, Staging.

Have a look at our website and Facebook page for an idea of what we do.
www.zoombr.com.au www.facebook.com/zoombrproductions

Be creative with the design, we are looking for something eye catching.

included are 4 different styles of our logo which we use. Take your pick of what you prefer.

Font styles to use
Serif
Sans Serif
Script

Requirements
Must have
• Eye catching, we are a design company creative events.
all the usual contact details etc.
Nice to have
• good use of colour
Should not have
• Nothing really....

```html
<!DOCTYPE html>
<html lang="en">
<head>
<meta charset="utf-8">
<title>Zoomb'r Business Cards</title>
<link href="https://fonts.googleapis.com/css2?family=Open+Sans:wght@400;600&display=swap" rel="stylesheet">
<style>
  :root {
    --page: #161616;
    --card-front: #1f1f20;
    --card-back: #2c2c2e;
    --card-edge: #3a3a3c;
    --text-light: #e6e6e6;
    --text-muted: #8a8a8c;
    --mark-faint: #2a2a2b;
  }
  * { margin: 0; padding: 0; box-sizing: border-box; }
  html, body { width: 1200px; height: 1200px; overflow: hidden; }
  body {
    background: var(--page);
    font-family: "Open Sans", sans-serif;
    display: flex;
    flex-direction: column;
    align-items: center;
    justify-content: center;
    gap: 60px;
  }
  .card {
    width: 840px;
    height: 480px;
    border: 3px solid var(--card-edge);
    position: relative;
    overflow: hidden;
  }
  .card--front {
    background: linear-gradient(160deg, #262627 0%, var(--card-front) 60%, #1a1a1b 100%);
  }
  .card--back { background: var(--card-back); }

  .front__name {
    position: absolute;
    top: 120px; left: 0; right: 0;
    text-align: center;
    font-size: 120px;
    font-weight: 600;
    color: var(--mark-faint);
    letter-spacing: 2px;
  }
  .front__services {
    position: absolute;
    bottom: 58px; left: 0; right: 0;
    text-align: center;
    color: var(--text-muted);
    text-transform: uppercase;
  }
  .front__intro { font-size: 13px; letter-spacing: 0.5px; margin-bottom: 8px; }
  .front__list { font-size: 19px; letter-spacing: 0.3px; }

  .back__brand {
    position: absolute;
    left: 80px; top: 200px;
    display: flex;
    align-items: center;
    gap: 18px;
  }
  .brand__square { width: 26px; height: 26px; background: var(--text-light); }
  .brand__name { font-size: 56px; font-weight: 600; color: var(--text-light); }

  .back__contact {
    position: absolute;
    left: 470px; top: 130px;
    color: var(--text-light);
    font-size: 18px;
    line-height: 1.5;
  }
  .contact__address { margin-bottom: 16px; }
  .contact__list { list-style: none; }
  .contact__item { display: flex; align-items: center; gap: 12px; margin-bottom: 4px; }
  .contact__icon { width: 16px; height: 16px; flex: none; }
</style>
</head>
<body>
  <section class="card card--front">
    <div class="front__name">Zoomb'r</div>
    <div class="front__services">
      <p class="front__intro">We hire out technical equipments</p>
      <p class="front__list">Lights, Special FX, Audio, Video, Projection, LED Screens, Rigging, Staging.</p>
    </div>
  </section>

  <section class="card card--back">
    <div class="back__brand">
      <span class="brand__square"></span>
      <span class="brand__name">Zoomb'r</span>
    </div>
    <div class="back__contact">
      <p class="contact__address">14/08 Harlow Lane, Westbridge<br>Vic 3390, Melbourne, Australia</p>
      <ul class="contact__list">
        <li class="contact__item">
          <svg class="contact__icon" viewBox="0 0 16 16"><path d="M3 1h3l1.5 4-2 1.3a8 8 0 0 0 4.2 4.2L11 8.5l4 1.5v3a2 2 0 0 1-2 2A12 12 0 0 1 1 3a2 2 0 0 1 2-2z" fill="#e6e6e6"/></svg>
          <span>+61 4 5550 2718</span>
        </li>
        <li class="contact__item">
          <svg class="contact__icon" viewBox="0 0 16 16"><rect x="1" y="3" width="14" height="10" fill="none" stroke="#e6e6e6" stroke-width="1.5"/><path d="M1 3l7 6 7-6" fill="none" stroke="#e6e6e6" stroke-width="1.5"/></svg>
          <span>info@zoombr.com.au</span>
        </li>
        <li class="contact__item">
          <svg class="contact__icon" viewBox="0 0 16 16"><circle cx="8" cy="8" r="6.5" fill="none" stroke="#e6e6e6" stroke-width="1.3"/><ellipse cx="8" cy="8" rx="3" ry="6.5" fill="none" stroke="#e6e6e6" stroke-width="1.1"/><path d="M1.5 8h13" stroke="#e6e6e6" stroke-width="1.1"/></svg>
          <span>www.zoombr.com.au/</span>
        </li>
        <li class="contact__item">
          <svg class="contact__icon" viewBox="0 0 16 16"><rect x="1" y="1" width="14" height="14" rx="2" fill="#e6e6e6"/></svg>
          <span>/zoombrproductions</span>
        </li>
      </ul>
    </div>
  </section>
</body>
</html>
```